Easy one-page Web Design with ready made sketch/template

This project have an already made one page Web Design sketch/template that should be used as a base. It needs professional touch and improvements but should be quite straight forward for you to make.

Webpage: Offers local graphical design services

Attached following documents for you:
- PSD sketch
- JPG sketch
- Word file with project description (read carefully)
- Logo

Target Market(s)

Logo design

Industry/Entity Type

Graphic Design

Number of Pages Required

1 page

Requirements
Must have
• Please refer to attached word document.
Nice to have
Should not have

```html
<!DOCTYPE html>
<html lang="sv">
<head>
<meta charset="utf-8">
<title>Märkesateljén – Logotypdesign</title>
<link rel="stylesheet" href="https://fonts.googleapis.com/css2?family=Lato:wght@400;700;900&display=swap">
<style>
:root{
  --blue:#2a9fd8;
  --card-head:#3aa3df;
  --card-body:#d6dde3;
  --orange:#ec7d0c;
  --yellow:#fbb63b;
  --green:#3d8d2e;
  --green-btn:#2f8a1f;
  --lime:#7cbd3c;
  --red:#e0202a;
  --paper:#e6e4dd;
  --ink:#3c3c3c;
  --cream:#fdfcc9;
  --white:#fff;
}
*{box-sizing:border-box;margin:0;padding:0}
html,body{width:1066px;height:1200px;overflow:hidden;background:var(--white);font-family:'Lato',sans-serif;color:var(--ink)}
.page{position:relative;width:1066px;height:1200px}

/* header */
.site-header{position:absolute;left:0;top:0;width:1066px;height:134px;background:var(--paper);box-shadow:0 2px 3px rgba(0,0,0,.35)}
.brand{position:absolute;left:216px;top:22px}
.brand-name{font-weight:900;font-size:27px;line-height:28px;color:#5a6670;letter-spacing:.5px}
.brand-name .sq{display:inline-block;width:12px;height:12px;background:var(--blue);margin-right:6px;vertical-align:middle}
.brand-tagline{position:absolute;left:218px;top:91px;font-weight:900;font-size:14px;line-height:13px;color:var(--blue);letter-spacing:.3px}
.main-nav{position:absolute;left:446px;top:72px;display:flex;gap:10px;font-size:17px;color:#666}
.call{position:absolute;right:212px;top:34px;font-size:14px;color:var(--blue)}
.order-btn{position:absolute;left:756px;top:70px;width:99px;height:24px;background:var(--orange);color:var(--white);font-size:12px;display:flex;align-items:center;justify-content:center;gap:5px;border:1px solid #f8a850}
.header-rule{position:absolute;left:0;top:163px;width:1066px;height:1px;background:#eee}

/* hero */
.hero{position:absolute;left:214px;top:136px;width:640px;height:428px;background:linear-gradient(180deg,#e9e9e9 0%,#d9d9d9 55%,#c9c9c9 100%)}
.hero-title{position:absolute;left:0;width:640px;top:38px;text-align:center;font-size:25px;font-weight:400;color:var(--blue);letter-spacing:.6px}
.hero-sub{position:absolute;left:0;width:640px;top:76px;text-align:center;font-size:12.5px;color:var(--lime);letter-spacing:.3px}
.hero-note{position:absolute;left:0;width:640px;top:101px;text-align:center;font-size:7px;color:var(--red)}
.from-btn{position:absolute;left:270px;top:130px;width:99px;height:24px;background:var(--green-btn);color:var(--white);font-size:12px;display:flex;align-items:center;justify-content:center;border:1px solid #e8f0e0}
.hero-books{position:absolute;left:60px;top:120px;width:90px;height:200px;background:linear-gradient(90deg,#f2f2f2,#d8d8d8)}
.hero-calendar{position:absolute;left:496px;top:190px;width:110px;height:160px;background:linear-gradient(180deg,#3a3a3a,#222)}
.video{position:absolute;left:144px;top:170px;width:350px;height:203px;background:#f5f5f5;box-shadow:0 0 4px rgba(0,0,0,.15)}
.video-screen{position:absolute;left:34px;top:12px;width:283px;height:165px;border:1px solid #999;border-radius:6px;background:linear-gradient(180deg,#fafafa,#ececec)}
.video-bar{position:absolute;left:0;bottom:0;width:350px;height:14px;background:linear-gradient(180deg,#444,#111)}
.video-progress{position:absolute;left:6px;bottom:15px;width:140px;height:2px;background:var(--red)}

/* features */
.feature{position:absolute;color:var(--white);text-align:center}
.feature-guarantee{left:214px;top:563px;width:185px;height:103px;background:var(--yellow)}
.feature-delivery{left:399px;top:546px;width:255px;height:128px;background:var(--orange)}
.feature-delivery::after{content:"";position:absolute;left:107px;bottom:-20px;border-left:21px solid transparent;border-right:21px solid transparent;border-top:20px solid var(--orange)}
.feature-rating{left:654px;top:562px;width:200px;height:104px;background:var(--green)}
.seal{position:absolute;left:55px;top:12px;width:74px;height:74px;border-radius:50%;background:#2b64b0;border:5px solid #c9d3e6}
.delivery-title{margin-top:20px;font-size:15px;letter-spacing:.8px}
.delivery-icon{margin:10px auto 0;display:block}
.delivery-price{margin-top:10px;font-size:11.5px;letter-spacing:.5px}
.rating-text{margin-top:13px;font-size:12px;font-weight:700;line-height:14.5px;letter-spacing:.4px}
.rating-badge{margin:7px auto 0;width:97px;height:46px;background:var(--white);box-shadow:0 1px 2px rgba(0,0,0,.3)}

/* packages */
.packages-title{position:absolute;left:0;width:1066px;top:726px;text-align:center;font-size:21px;font-weight:900;letter-spacing:1px;color:var(--ink)}
.packages-sub{position:absolute;left:0;width:1066px;top:757px;text-align:center;font-size:12px;font-weight:900;letter-spacing:1px;color:var(--blue)}
.card{position:absolute;top:834px;width:148px;height:324px;background:var(--card-body)}
.card-head{height:38px;background:var(--card-head);color:var(--white);font-size:16px;letter-spacing:.8px;display:flex;align-items:center;justify-content:center}
.price{text-align:center;font-size:23px;color:var(--blue);margin-top:19px;line-height:22px;letter-spacing:.5px}
.vat{text-align:center;font-size:8px;color:var(--orange);font-weight:700;letter-spacing:.5px}
.features{list-style:none;position:absolute;left:17px;right:8px}
.features li{position:relative;padding-left:15px;font-size:9px;line-height:15.4px;color:#333}
.features li::before{content:"✸";position:absolute;left:0;top:0;font-size:9px;color:#333}
.card-starter .features li{font-size:12px;line-height:15.4px}
.card-platinum .features li{font-size:7.5px}
.order-note{position:absolute;left:17px;top:252px;font-size:9px;line-height:15.4px;color:#333}
.card-btn{position:absolute;top:284px;width:115px;height:30px;background:var(--blue);color:var(--white);font-size:12px;letter-spacing:.6px;display:flex;align-items:center;justify-content:center}
.card-starter{left:214px}
.card-silver{left:368px}
.card-platinum{left:705px}
.card-unlimited{position:absolute;left:520px;top:798px;width:180px;height:396px;background:var(--cream)}
.card-unlimited .card-head{position:absolute;left:17px;top:12px;width:149px;height:39px;background:var(--orange)}
.card-unlimited .price{position:absolute;left:0;width:180px;top:61px;margin:0}
.card-unlimited .vat{position:absolute;left:0;width:180px;top:85px}
.card-unlimited .features li::before{color:var(--orange)}
.offer{position:absolute;left:0;width:180px;top:333px;text-align:center;font-size:9px;color:#333}
.card-unlimited .card-btn{left:33px;top:355px;background:var(--orange)}
</style>
</head>
<body>
<div class="page">
  <header class="site-header">
    <div class="brand"><div class="brand-name"><span class="sq"></span>MÄRKES<br>ATELJÉN</div></div>
    <div class="brand-tagline">PROFESSIONELL DESIGN<br>TILL "INTERNETPRIS"</div>
    <nav class="main-nav"><span>Products</span><span>Gallery</span><span>FAQ</span><span>Contact us</span></nav>
    <div class="call">Call us 08-555 010 20</div>
    <div class="order-btn">
      <svg width="12" height="11" viewBox="0 0 12 11"><path d="M0 1h2l2 6h6l1.5-4H3" fill="none" stroke="#fff" stroke-width="1.4"/><circle cx="4.5" cy="9.5" r="1" fill="#fff"/><circle cx="9.5" cy="9.5" r="1" fill="#fff"/></svg>
      Order Logo
    </div>
  </header>
  <div class="header-rule"></div>

  <section class="hero">
    <div class="hero-books" role="img" aria-label="Designböcker på skrivbordet"></div>
    <div class="hero-calendar" role="img" aria-label="Bordskalender"></div>
    <h1 class="hero-title">Ny Logotyp / Företagslogga?</h1>
    <p class="hero-sub">Ha din nya logotyp design klar redan imorgon!</p>
    <p class="hero-note">Vi skräddarsyr din professionella företagslogotyp och skickar dig första utkasten redan inom 24-timmar</p>
    <div class="from-btn">FRÅN 1495</div>
    <div class="video">
      <div class="video-screen" role="img" aria-label="Videoklipp med exempel på kundlogotyper på en bärbar dator"></div>
      <div class="video-progress"></div>
      <div class="video-bar"></div>
    </div>
  </section>

  <div class="feature feature-guarantee"><div class="seal" role="img" aria-label="Nöjd-kund-garanti"></div></div>
  <div class="feature feature-delivery">
    <div class="delivery-title">Delivery within 24-hours</div>
    <svg class="delivery-icon" width="56" height="40" viewBox="0 0 56 40" fill="none" stroke="#fff" stroke-width="3">
      <path d="M2 4h30v24H2z"/><path d="M32 12h12l8 9v7H32z"/><circle cx="13" cy="32" r="5" fill="var(--orange)"/><circle cx="42" cy="32" r="5" fill="var(--orange)"/>
    </svg>
    <div class="delivery-price">from 1495 FR</div>
  </div>
  <div class="feature feature-rating">
    <div class="rating-text">9.7/10 rating on ReviewHub<br>200+ customer reviews</div>
    <div class="rating-badge" role="img" aria-label="Omdömesbetyg"></div>
  </div>

  <h2 class="packages-title">SELECT A PACKAGE</h2>
  <div class="packages-sub">FIXED PRICE</div>

  <div class="card card-starter">
    <div class="card-head">STARTER</div>
    <div class="price">1495,-</div><div class="vat">( +MOMS )</div>
    <ul class="features" style="top:117px">
      <li>3 logotyputkast</li><li>1 ändring/revision</li><li>Filer för webben</li>
    </ul>
    <div class="order-note">Beställ nu!<br>GRATIS Vänsidan-logga*</div>
    <div class="card-btn" style="left:17px">BESTALL</div>
  </div>

  <div class="card card-silver">
    <div class="card-head">SILVER</div>
    <div class="price">2495,-</div><div class="vat">( +MOMS )</div>
    <ul class="features" style="top:117px">
      <li>6 logotyputkast</li><li>3 ändringar/revisioner</li><li>Filer för webben</li><li>Vektorgrafiska filer för tryck</li>
    </ul>
    <div class="order-note">Beställ nu!<br>GRATIS Vänsidan-logga*</div>
    <div class="card-btn" style="left:10px">BESTALL</div>
  </div>

  <div class="card-unlimited">
    <div class="card-head">UNLIMITED</div>
    <div class="price">9995,-</div><div class="vat">( +MOMS )</div>
    <ul class="features" style="top:112px;left:26px">
      <li>100% nöjdhetsgaranti</li><li>10 logotyputkast</li><li>Obergränsat med ändringar/revisioner</li><li>Allt du behöver ingår</li><li>Visitkort design</li><li>Brevpapper design</li><li>Logotypguide</li><li>Telefonsupport</li><li>Vänsidan logotyp</li><li>Webb &amp; tryckfiler ingår</li><li>BESTÄLL IDAG: Få en bonusprodukt (värde 495kr)</li>
    </ul>
    <div class="offer">Erbjudandet gäller</div>
    <div class="card-btn">BESTALL</div>
  </div>

  <div class="card card-platinum">
    <div class="card-head">PLATINUM</div>
    <div class="price">9995,-</div><div class="vat">( +MOMS )</div>
    <ul class="features" style="top:103px;left:14px">
      <li>Allt i Unlimited paketet</li><li>Proffsig hemsida som enkelt uppdaterar</li><li>Responsiv Design ( för mobiler och läsplattor )</li><li>490kr/mån (ingen bindningstid)</li><li>1-tim support per månad</li><li>Full grafisk profil för dig som vil ha en rivstart!</li>
    </ul>
    <div class="order-note" style="top:251px">Beställ nu!<br>GRATIS Vänsidan-logga*</div>
    <div class="card-btn" style="left:17px;top:285px">BESTALL</div>
  </div>
</div>
</body>
</html>
```